Infographics for Quorvel reports

Quorvel report is a summary of software developer skills.

Main purpose of our reports is to provide quick and easy insight into skill set of tested individual.
Our mission is to help talents to stand out.

Our target market is a male between 25-40, bit of a nerd, who likes technology and computer games.
The report should communicate quality and trust.

Report should fit on one A4 page and contain the following
1. Company logo - provided with the brief

2. Information about tested developer:
- Photo of developer
- Full name
- Location
- Email

3. How he or she compares against the average Software Developer:
- Collaboration ranking (0-100)
- Skills ranking by languages (up to 10 languages)

4. Total ranking - Number 1-100% which should stand out as a quick reference

We would like to included some sort of stamp of approval on the report.
The stamp would contain the overall score of a developer (The Total ranking from point 4.) .

As an option we were considering to use some sort of categorisation for the total ranking.
Here are examples of Quorvel categories:
Wizard of Quorvel for ranking between 90% – 100%
Scholar of Quorvel for ranking between 80% - 89%
Knight of Quorvel for ranking between 70% - 79%
Warrior of Quorvel for ranking between 60% - 69%
Rebel of Quorvel unknown or under 60%

Developer would belong to one of the categories depending on their Total ranking.

We are not very fixed on category names. We would be happy to consider any other option.

Here are some example data for the report:

The average Software Developer ranking is 50%.

Tested Developer:
Photo
Full name: Mark Tester
Location: Sydney, Australia
Email: mark.tester@mailvex.com

Collaboration ranking: 95%

Skills:
Language: C++
Number of Open Source Projects: 5
Ranking: 91%

Language: Javascript
Number of Open Source Projects: 3
Ranking: 81%

Language: Python
Number of Open Source Projects: 1
Ranking: 31%

Language: Ruby
Number of Open Source Projects: 2
Ranking: 25%

Language: C#
Ranking: 85%

Language: Java
Ranking: 75%

Total Ranking: 75% - Knight of Quorvel

Thank you!

```html
<!DOCTYPE html>
<html lang="en">
<head>
<meta charset="utf-8">
<title>Quorvel Report – Mark Tester</title>
<link href="https://fonts.googleapis.com/css2?family=Arimo:ital,wght@0,400;0,700;1,400&display=swap" rel="stylesheet">
<style>
  :root{
    --purple:#8c2a78;
    --purple-dark:#5e1a50;
    --ink:#111111;
    --grey:#e5e5e7;
    --grey-mid:#c9c9cc;
    --rule:#8a8a8a;
    --paper:#ffffff;
  }
  *{box-sizing:border-box;margin:0;padding:0}
  html,body{width:848px;height:1200px;overflow:hidden;background:var(--paper)}
  body{font-family:"Arimo",Arial,sans-serif;color:var(--ink)}
  .report{position:relative;width:848px;height:1200px;overflow:hidden;background:var(--paper)}

  /* Header */
  .brand{position:absolute;left:43px;top:52px;display:flex;align-items:center;height:62px}
  .brand-mark{width:30px;height:30px;background:var(--purple);margin-right:12px}
  .brand-name{font-weight:700;font-size:50px;letter-spacing:-1px;color:var(--ink)}
  .brand-divider{width:3px;height:50px;background:var(--ink);margin:0 12px}
  .brand-title{font-weight:700;font-size:50px;letter-spacing:-1px;color:var(--ink)}

  /* Profile */
  .profile-photo{position:absolute;left:40px;top:168px;width:239px;height:237px;background:var(--purple)}
  .profile-name{position:absolute;left:303px;top:176px;font-size:50px;font-weight:700;letter-spacing:-0.5px}
  .profile-location{position:absolute;left:312px;top:244px;font-size:25px;display:flex;align-items:center;gap:14px}
  .profile-email{position:absolute;left:312px;top:280px;font-size:25px}
  .profile-email b{color:var(--purple)}

  .legend-bar{position:absolute;left:26px;top:345px;width:801px;height:37px;background:var(--ink)}
  .legend-fold{position:absolute;left:26px;top:382px;width:14px;height:14px;background:#555;clip-path:polygon(0 0,100% 0,100% 100%)}
  .legend{position:absolute;left:302px;top:355px;display:flex;gap:18px;color:#fff;font-size:12.5px;align-items:center}
  .legend span{display:flex;align-items:center;gap:5px}

  /* Skills */
  .skill{position:absolute;width:225px;height:100px}
  .skill-icon{position:absolute;left:10px;top:19px;width:40px;height:40px;background:var(--ink);transform:rotate(45deg)}
  .skill-icon span{position:absolute;inset:0;display:flex;align-items:center;justify-content:center;transform:rotate(-45deg);color:#fff;font-weight:700;font-size:12px;font-style:normal}
  .skill-projects-icon{position:absolute;left:75px;top:0;width:29px;height:26px}
  .skill-projects{position:absolute;right:0;top:-6px;font-size:34px;font-style:italic}
  .skill-rule{position:absolute;left:75px;right:0;top:40px;border-top:1.5px dotted var(--rule)}
  .skill-ring{position:absolute;left:75px;top:50px;width:29px;height:29px}
  .skill-rank{position:absolute;right:0;top:45px;font-size:34px;font-style:italic}

  /* Collaboration */
  .figure{position:absolute;background:var(--purple);border-radius:30px 30px 8px 8px}
  .figure-left{left:114px;top:1019px;width:70px;height:135px}
  .figure-right{left:330px;top:1019px;width:62px;height:135px}
  .collab-label{position:absolute;left:188px;top:1047px;width:138px;text-align:center;font-size:12.5px;line-height:1.15}
  .collab-value{position:absolute;left:188px;top:1086px;width:138px;text-align:center;font-size:44px;font-weight:700}

  /* Stamp */
  .stamp-banner{position:absolute;left:453px;top:988px;width:355px;height:32px;background:var(--purple);color:#fff;font-weight:700;font-size:18px;letter-spacing:5px;display:flex;align-items:center;justify-content:center}
  .stamp-fold{position:absolute;top:1020px;width:10px;height:10px;background:var(--purple-dark)}
  .stamp-fold.left{left:453px;clip-path:polygon(0 0,100% 0,100% 100%)}
  .stamp-fold.right{left:798px;clip-path:polygon(0 0,100% 0,0 100%)}
  .stamp-box{position:absolute;left:463px;top:1020px;width:335px;height:137px;background:var(--grey);display:flex;align-items:center;justify-content:center}
  .stamp-score{font-size:124px;font-weight:700;letter-spacing:-3px;line-height:1}

  /* Footer */
  .footer{position:absolute;left:0;top:1178px;width:848px;height:22px;background:var(--ink);color:#fff;font-size:9px;display:flex;justify-content:space-between;align-items:center;padding:0 40px 0 66px}
</style>
</head>
<body>
<svg width="0" height="0" style="position:absolute" aria-hidden="true">
  <defs>
    <pattern id="dots-grey" width="6" height="5.2" patternUnits="userSpaceOnUse"><circle cx="3" cy="2.6" r="2" fill="#c9c9cc"/></pattern>
    <pattern id="dots-purple" width="6" height="5.2" patternUnits="userSpaceOnUse"><circle cx="3" cy="2.6" r="2" fill="#8c2a78"/></pattern>
  </defs>
</svg>

<main class="report">
  <header class="brand">
    <span class="brand-mark"></span>
    <span class="brand-name">Quorvel</span>
    <span class="brand-divider"></span>
    <span class="brand-title">Report</span>
  </header>

  <div class="profile-photo" role="img" aria-label="Photo of the developer"></div>
  <h1 class="profile-name">Mark Tester</h1>
  <p class="profile-location">
    <svg width="16" height="24" viewBox="0 0 16 24"><path d="M8 0C3.6 0 0 3.5 0 7.8 0 13.5 8 24 8 24s8-10.5 8-16.2C16 3.5 12.4 0 8 0z" fill="var(--purple)"/><circle cx="8" cy="8" r="3" fill="#fff"/></svg>
    Sydney, Australia
  </p>
  <p class="profile-email"><b>e:</b> mark.tester@mailvex.com</p>

  <div class="legend-bar"></div>
  <div class="legend-fold"></div>
  <div class="legend">
    <span><svg width="14" height="14" viewBox="0 0 20 20"><circle cx="10" cy="10" r="7" fill="none" stroke="#777" stroke-width="4"/><circle cx="10" cy="10" r="7" fill="none" stroke="#fff" stroke-width="4" stroke-dasharray="33 44" transform="rotate(-90 10 10)"/></svg>Ranking</span>
    <span><svg width="14" height="12"><rect width="14" height="12" fill="url(#dots-grey)"/></svg>Number of Projects</span>
    <span><svg width="14" height="14" viewBox="0 0 14 14"><rect x="2.5" y="2.5" width="9" height="9" fill="var(--purple)" transform="rotate(45 7 7)"/></svg>Language Skills</span>
  </div>

  <!-- Left column -->
  <section class="skill" style="left:110px;top:467px">
    <div class="skill-icon"><span style="font-size:14px">C++</span></div>
    <svg class="skill-projects-icon"><rect width="29" height="26" fill="url(#dots-purple)"/></svg>
    <div class="skill-projects">5</div><div class="skill-rule"></div>
    <svg class="skill-ring" viewBox="0 0 20 20"><circle cx="10" cy="10" r="7" fill="none" stroke="var(--grey-mid)" stroke-width="3.5"/><circle cx="10" cy="10" r="7" fill="none" stroke="var(--purple)" stroke-width="3.5" stroke-dasharray="40 44" transform="rotate(-90 10 10)"/></svg>
    <div class="skill-rank">91%</div>
  </section>

  <section class="skill" style="left:110px;top:587px">
    <div class="skill-icon"><span style="font-size:11px">Java</span></div>
    <svg class="skill-projects-icon"><rect width="29" height="10.4" fill="url(#dots-grey)"/><rect y="10.4" width="29" height="15.6" fill="url(#dots-purple)"/></svg>
    <div class="skill-projects">3</div><div class="skill-rule"></div>
    <svg class="skill-ring" viewBox="0 0 20 20"><circle cx="10" cy="10" r="7" fill="none" stroke="var(--grey-mid)" stroke-width="3.5"/><circle cx="10" cy="10" r="7" fill="none" stroke="var(--purple)" stroke-width="3.5" stroke-dasharray="35.6 44" transform="rotate(-90 10 10)"/></svg>
    <div class="skill-rank">81%</div>
  </section>

  <section class="skill" style="left:110px;top:705px">
    <div class="skill-icon"><span>Py</span></div>
    <svg class="skill-projects-icon"><rect width="29" height="20.8" fill="url(#dots-grey)"/><rect y="20.8" width="29" height="5.2" fill="url(#dots-purple)"/></svg>
    <div class="skill-projects">1</div><div class="skill-rule"></div>
    <svg class="skill-ring" viewBox="0 0 20 20"><circle cx="10" cy="10" r="7" fill="none" stroke="var(--grey-mid)" stroke-width="3.5"/><circle cx="10" cy="10" r="7" fill="none" stroke="var(--purple)" stroke-width="3.5" stroke-dasharray="13.6 44" transform="rotate(-90 10 10)"/></svg>
    <div class="skill-rank">31%</div>
  </section>

  <section class="skill" style="left:110px;top:826px">
    <div class="skill-icon"><span>Rb</span></div>
    <svg class="skill-projects-icon"><rect width="29" height="15.6" fill="url(#dots-grey)"/><rect y="15.6" width="29" height="10.4" fill="url(#dots-purple)"/></svg>
    <div class="skill-projects">2</div><div class="skill-rule"></div>
    <svg class="skill-ring" viewBox="0 0 20 20"><circle cx="10" cy="10" r="7" fill="none" stroke="var(--grey-mid)" stroke-width="3.5"/><circle cx="10" cy="10" r="7" fill="none" stroke="var(--purple)" stroke-width="3.5" stroke-dasharray="11 44" transform="rotate(-90 10 10)"/></svg>
    <div class="skill-rank">25%</div>
  </section>

  <!-- Right column -->
  <section class="skill" style="left:484px;top:467px">
    <div class="skill-icon"><span>AS3</span></div>
    <svg class="skill-projects-icon"><rect width="29" height="10.4" fill="url(#dots-grey)"/><rect y="10.4" width="29" height="15.6" fill="url(#dots-purple)"/></svg>
    <div class="skill-projects">3</div><div class="skill-rule"></div>
    <svg class="skill-ring" viewBox="0 0 20 20"><circle cx="10" cy="10" r="7" fill="none" stroke="var(--grey-mid)" stroke-width="3.5"/><circle cx="10" cy="10" r="7" fill="none" stroke="var(--purple)" stroke-width="3.5" stroke-dasharray="37.4 44" transform="rotate(-90 10 10)"/></svg>
    <div class="skill-rank">85%</div>
  </section>

  <section class="skill" style="left:484px;top:587px">
    <div class="skill-icon"><span style="font-size:16px">JS</span></div>
    <svg class="skill-projects-icon"><rect width="29" height="26" fill="url(#dots-purple)"/></svg>
    <div class="skill-projects">5</div><div class="skill-rule"></div>
    <svg class="skill-ring" viewBox="0 0 20 20"><circle cx="10" cy="10" r="7" fill="none" stroke="var(--grey-mid)" stroke-width="3.5"/><circle cx="10" cy="10" r="7" fill="none" stroke="var(--purple)" stroke-width="3.5" stroke-dasharray="33 44" transform="rotate(-90 10 10)"/></svg>
    <div class="skill-rank">75%</div>
  </section>

  <section class="skill" style="left:484px;top:705px">
    <div class="skill-icon"><span style="font-size:20px">C</span></div>
    <svg class="skill-projects-icon"><rect width="29" height="5.2" fill="url(#dots-grey)"/><rect y="5.2" width="29" height="20.8" fill="url(#dots-purple)"/></svg>
    <div class="skill-projects">4</div><div class="skill-rule"></div>
    <svg class="skill-ring" viewBox="0 0 20 20"><circle cx="10" cy="10" r="7" fill="none" stroke="var(--grey-mid)" stroke-width="3.5"/><circle cx="10" cy="10" r="7" fill="none" stroke="var(--purple)" stroke-width="3.5" stroke-dasharray="22 44" transform="rotate(-90 10 10)"/></svg>
    <div class="skill-rank">50%</div>
  </section>

  <section class="skill" style="left:484px;top:826px">
    <div class="skill-icon"><span>PHP</span></div>
    <svg class="skill-projects-icon"><rect width="29" height="10.4" fill="url(#dots-grey)"/><rect y="10.4" width="29" height="15.6" fill="url(#dots-purple)"/></svg>
    <div class="skill-projects">3</div><div class="skill-rule"></div>
    <svg class="skill-ring" viewBox="0 0 20 20"><circle cx="10" cy="10" r="7" fill="none" stroke="var(--grey-mid)" stroke-width="3.5"/><circle cx="10" cy="10" r="7" fill="none" stroke="var(--purple)" stroke-width="3.5" stroke-dasharray="33 44" transform="rotate(-90 10 10)"/></svg>
    <div class="skill-rank">75%</div>
  </section>

  <!-- Collaboration -->
  <div class="figure figure-left" role="img" aria-label="Figure of a person walking"></div>
  <div class="figure figure-right" role="img" aria-label="Figure of a person walking"></div>
  <p class="collab-label">COLLABORATION<br>RANKING</p>
  <p class="collab-value">95%</p>

  <!-- Stamp -->
  <div class="stamp-banner">KNIGHT OF QUORVEL</div>
  <div class="stamp-fold left"></div>
  <div class="stamp-fold right"></div>
  <div class="stamp-box"><span class="stamp-score">76%</span></div>

  <footer class="footer"><span>© 2014 Quorvel</span><span>All rights Reserved</span></footer>
</main>
</body>
</html>
```